Business Card Design Project

I want a cleaner business card and envelope then what we have now, its too crowded.
Updates

I update with logo, this can be changed anyway you feel it looks best. I also have put gaurantee on there and extended time, this is my first time doing this. Also gave an example of current card

Target Market(s)

a wide array of customers from lattice 700 to small companies and cleints

Industry/Entity Type

Business

Requirements
Must have
• Need to have address, telephone number email
Nice to have
• a sharp professional card that stands out but is still very clean.
Should not have
• Not crazy looking

```html
<!DOCTYPE html>
<html lang="en">
<head>
<meta charset="utf-8">
<title>Halvern Insurance Group – Business Card</title>
<link href="https://fonts.googleapis.com/css2?family=Open+Sans:wght@400;700&display=swap" rel="stylesheet">
<style>
  :root{
    --page:#e9e6e1;
    --card-white:#ffffff;
    --card-dark:#3a3a3c;
    --card-mid:#6b6b6d;
    --ink:#2b2b2d;
    --on-dark:#f2f2f2;
  }
  *{margin:0;padding:0;box-sizing:border-box}
  html,body{width:1200px;height:1023px;overflow:hidden}
  body{
    background:var(--page);
    font-family:"Open Sans",Arial,sans-serif;
    display:flex;flex-direction:column;align-items:center;justify-content:center;gap:60px;
  }
  .card{
    position:relative;width:620px;height:354px;overflow:hidden;
    background:var(--card-white);
    box-shadow:0 10px 28px rgba(0,0,0,.22);
  }
  .card__shape{position:absolute;inset:0;width:100%;height:100%}
  .services{
    position:absolute;top:30px;left:34px;right:24px;
    display:flex;justify-content:space-between;color:var(--on-dark);
  }
  .services__title{font-size:11px;font-weight:700;letter-spacing:.04em;text-transform:uppercase;margin-bottom:5px;white-space:nowrap}
  .services__list{list-style:none;font-size:10.5px;line-height:1.55;white-space:nowrap}
  .services__list li::before{content:"•";margin-right:5px}
  .brand{
    position:absolute;left:42px;bottom:38px;display:flex;align-items:center;gap:14px;
    color:var(--ink);
  }
  .brand__square{width:46px;height:46px;background:var(--card-mid)}
  .brand__name{font-size:20px;font-weight:700;letter-spacing:.12em;line-height:1.2;text-transform:uppercase}
  .contact{
    position:absolute;top:52px;left:48px;color:var(--on-dark);
    font-size:13px;line-height:1.7;
  }
  .contact__name{font-size:17px;font-weight:700;letter-spacing:.06em;margin-bottom:6px}
</style>
</head>
<body>

  <section class="card card--front" aria-label="Card front">
    <svg class="card__shape" viewBox="0 0 620 354" preserveAspectRatio="none" aria-hidden="true">
      <path d="M0,0 H620 V354 C600,262 520,200 400,196 C260,192 120,205 0,228 Z" fill="var(--card-dark)"/>
    </svg>
    <div class="services">
      <div class="services__group">
        <h3 class="services__title">Commercial Insurance</h3>
        <ul class="services__list">
          <li>Traditional Insurance Coverage</li>
          <li>Executive Protection Coverage</li>
          <li>Specialty Coverage Insurance</li>
        </ul>
      </div>
      <div class="services__group">
        <h3 class="services__title">Personal Insurance</h3>
        <ul class="services__list">
          <li>Auto/Recreational/Boat</li>
          <li>Home/Renters/Condo</li>
          <li>Umbrella Liability</li>
        </ul>
      </div>
      <div class="services__group">
        <h3 class="services__title">Employee Benefits</h3>
        <ul class="services__list">
          <li>Medical/Dental/Optical Plans</li>
          <li>Prescription Coverage</li>
          <li>Life &amp; Accidental Death</li>
          <li>&amp; Dismemberment Insurance</li>
          <li>Disability Insurance</li>
          <li>Voluntary Benefits</li>
        </ul>
      </div>
    </div>
    <div class="brand">
      <span class="brand__square"></span>
      <span class="brand__name">Halvern<br>Insurance Group</span>
    </div>
  </section>

  <section class="card card--back" aria-label="Card back">
    <svg class="card__shape" viewBox="0 0 620 354" preserveAspectRatio="none" aria-hidden="true">
      <rect x="0" y="0" width="620" height="215" fill="var(--card-dark)"/>
      <path d="M470,215 L620,215 L620,354 L410,354 Z" fill="var(--card-mid)"/>
    </svg>
    <div class="contact">
      <p class="contact__name">Dana Reyes, Agent</p>
      <p>42560 Harbor Road</p>
      <p>Halvern Heights, MI 48310</p>
      <p>Tel 555-014-2290</p>
      <p>dana@halverngroup.com</p>
    </div>
  </section>

</body>
</html>
```